Kentucky residential recovery center needs a flyer design

We need a flyer design for a 16 bed male residential/inpatient recovery center based in Richmond, Kentucky. The facility provides short term (average 30 day) treatment to those struggling with substace abuse and addiction. The design should communicate trust, assurance, safety.
Our wesite provides more information https://morvalcare.org/treatment-services/residential-treatment/

Target Market(s)

Men (typically 30-50) struggling with substance addiction

```html
<!DOCTYPE html>
<html lang="en">
<head>
<meta charset="utf-8">
<title>Morval Care – Residential Treatment Flyer</title>
<link href="https://fonts.googleapis.com/css2?family=Montserrat:wght@400;500;600;700;800&display=swap" rel="stylesheet">
<style>
  :root{
    --navy:#2f2b70;
    --navy-deep:#27235f;
    --green:#1e9a3e;
    --ink:#2c2c3a;
    --paper:#fbfbfb;
    --stage:#9dcbea;
    --photo-light:#e7eef4;
    --photo-mid:#bcd3e6;
  }
  *{box-sizing:border-box;margin:0;padding:0}
  html,body{width:1200px;height:900px;overflow:hidden}
  body{background:var(--stage);font-family:'Montserrat',sans-serif;position:relative}
  .flyer{position:absolute;left:293px;top:20px;width:613px;height:860px;background:var(--paper);overflow:hidden;box-shadow:0 8px 24px rgba(20,40,80,.25)}
  .top-band{position:absolute;left:0;top:0;width:613px;height:60px}
  .brand{position:absolute;left:38px;top:58px;display:flex;align-items:center;gap:8px}
  .brand-dot{width:26px;height:26px;border-radius:50%;background:var(--navy)}
  .brand-name{font-weight:700;font-size:17px;color:var(--navy);letter-spacing:.5px}
  .hero-photo{position:absolute;left:332px;top:16px;width:281px;height:273px}
  .hero-fill{position:absolute;inset:0 0 6px 4px;border-bottom-left-radius:60px;background:linear-gradient(135deg,var(--photo-mid),var(--photo-light) 55%,#f4f6f8)}
  .hero-frame{position:absolute;inset:0;border-left:3px solid var(--green);border-bottom:6px solid var(--green);border-bottom-left-radius:62px;pointer-events:none}
  .title{position:absolute;left:20px;top:150px;font-size:21.5px;font-weight:700;color:var(--green);letter-spacing:.2px}
  .intro{position:absolute;left:20px;top:178px;width:300px;font-size:12.3px;line-height:15.2px;color:var(--ink)}
  .kicker{position:absolute;left:20px;top:255px;font-size:15px;font-weight:600;color:var(--navy);letter-spacing:.3px}
  .section-head{position:absolute;font-size:21px;font-weight:700;color:var(--green);line-height:25px}
  .issues-head{left:20px;top:278px}
  .why-head{left:337px;top:300px}
  .issue{position:absolute;width:140px;text-align:center}
  .issue-photo{width:120px;height:120px;margin:0 auto;border-radius:50%;border:3px solid var(--navy);box-shadow:inset 0 0 0 3px #fff}
  .issue-label{margin-top:10px;font-size:12.5px;font-weight:600;color:#3a3a46;line-height:15px;letter-spacing:.3px}
  .p-alcohol{background:radial-gradient(circle at 40% 55%,#b07a3c,#6d5a4c 45%,#3b3f55)}
  .p-drugs{background:radial-gradient(circle at 50% 55%,#4a4a4e,#2a2a2e 70%)}
  .p-medication{background:radial-gradient(circle at 45% 50%,#9c8570,#4d4038 70%)}
  .p-behavioral{background:radial-gradient(circle at 40% 45%,#b98a6f,#e4dfdb 65%)}
  .card{position:absolute;background:var(--navy);border-radius:10px;color:#fff;padding:12px 9px 0 9px}
  .card svg{display:block;width:22px;height:22px;margin-bottom:7px}
  .card-title{font-size:10px;font-weight:700;line-height:12.5px;text-transform:uppercase}
  .card-text{margin-top:5px;font-size:10px;line-height:12.5px;color:#d9d8ee}
  .contact-icon{position:absolute;width:22px;height:22px;border-radius:50%;background:var(--navy);display:flex;align-items:center;justify-content:center}
  .contact-icon svg{width:12px;height:12px}
  .locations{position:absolute;left:60px;top:722px;font-size:12px;line-height:14.5px;color:var(--ink)}
  .loc-name{font-weight:700;color:var(--green);letter-spacing:.2px}
  .loc-gap{margin-top:2px}
  .contact-line{position:absolute;left:367px;font-size:12.3px;color:var(--ink);line-height:17px}
  .bottom-band{position:absolute;left:0;top:834px;width:613px;height:26px;background:var(--navy)}
</style>
</head>
<body>
<main class="flyer">
  <svg class="top-band" viewBox="0 0 613 60" aria-hidden="true">
    <polygon points="0,0 613,0 613,0 332,18 0,49" fill="var(--navy)"/>
  </svg>

  <div class="brand">
    <span class="brand-dot"></span>
    <span class="brand-name">MORVAL CARE</span>
  </div>

  <div class="hero-photo">
    <div class="hero-fill" role="img" aria-label="Photo of a smiling doctor in a white coat with a stethoscope, colleagues in the background"></div>
    <div class="hero-frame"></div>
  </div>

  <h1 class="title">RESIDENTIAL TREATMENT</h1>
  <p class="intro">Inpatient Treatment,also Refered to as Resdential Treatment,Provides the Highest Level of Rehab Service for Patients Diaganosed with Alcohol,The Drug or Substance Addication</p>

  <p class="kicker">PROBLEMS WE CAN HELP WITH</p>
  <h2 class="section-head issues-head">WHAT ISSUES CAN<br>BE TREATED?</h2>

  <div class="issue" style="left:11px;top:343px">
    <div class="issue-photo p-alcohol" role="img" aria-label="Photo of a glass of whiskey on a table"></div>
    <p class="issue-label">ALCOHOLISM</p>
  </div>
  <div class="issue" style="left:155px;top:343px">
    <div class="issue-photo p-drugs" role="img" aria-label="Photo of hands holding pills among scattered cigarettes"></div>
    <p class="issue-label">DRUG ADDICTION</p>
  </div>
  <div class="issue" style="left:11px;top:499px">
    <div class="issue-photo p-medication" role="img" aria-label="Photo of a person holding pills and a glass of water"></div>
    <p class="issue-label">MEDICATION<br>ADDICTION</p>
  </div>
  <div class="issue" style="left:155px;top:499px">
    <div class="issue-photo p-behavioral" role="img" aria-label="Photo of a distressed woman holding her head, a helping hand reaching out"></div>
    <p class="issue-label">BEHAVIORAL<br>HEALTH</p>
  </div>

  <h2 class="section-head why-head">WHY CHOOSE US?</h2>

  <div class="card" style="left:334px;top:346px;width:114px;height:130px">
    <svg viewBox="0 0 24 24" fill="#fff" aria-hidden="true"><path d="M12 4 1 9l11 5 9-4.1V16h2V9z"/><path d="M6 13v4c0 1.5 3 3 6 3s6-1.5 6-3v-4l-6 2.7z"/></svg>
    <p class="card-title">100+<br>Years</p>
    <p class="card-text">Over 100 years of medical &amp; clinical experience behind our team</p>
  </div>
  <div class="card" style="left:475px;top:346px;width:115px;height:130px">
    <svg viewBox="0 0 24 24" fill="none" stroke="#fff" stroke-width="1.6" aria-hidden="true"><path d="M3 10h4v10H3z"/><path d="M7 10l4-7c1.5 0 2.5 1 2 3l-1 3h6c1.3 0 2.2 1.2 1.9 2.4l-1.6 6.4c-.3 1.1-1.2 2.2-2.4 2.2H7"/></svg>
    <p class="card-title">95%<br>Satisfation<br>Rating</p>
    <p class="card-text">Our patients rate us 95 out of 100</p>
  </div>
  <div class="card" style="left:334px;top:501px;width:114px;height:135px">
    <svg viewBox="0 0 24 24" fill="none" stroke="#fff" stroke-width="1.5" stroke-linejoin="round" aria-hidden="true"><path d="M12 2.5l2.9 6.2 6.6.7-4.9 4.5 1.4 6.6L12 17.2l-6 3.3 1.4-6.6-4.9-4.5 6.6-.7z"/></svg>
    <p class="card-title">#1 Best Drug &amp; Alcohol Rehab Center</p>
    <p class="card-text">Voted one of the best Alcohol and Drug rehab centers</p>
  </div>
  <div class="card" style="left:475px;top:501px;width:115px;height:135px">
    <svg viewBox="0 0 24 24" fill="none" stroke="#fff" stroke-width="1.6" aria-hidden="true"><path d="M12 20s-8-5-8-11a4.5 4.5 0 0 1 8-2.8A4.5 4.5 0 0 1 20 9c0 6-8 11-8 11z"/></svg>
    <p class="card-title">2,500+ Patients Treated</p>
    <p class="card-text">Over 2,500 patients treated successfully and counting</p>
  </div>

  <div class="contact-icon" style="left:23px;top:723px">
    <svg viewBox="0 0 24 24" fill="#fff" aria-hidden="true"><path d="M12 2a7 7 0 0 0-7 7c0 5 7 13 7 13s7-8 7-13a7 7 0 0 0-7-7zm0 9.5A2.5 2.5 0 1 1 12 6.5a2.5 2.5 0 0 1 0 5z"/></svg>
  </div>
  <div class="locations">
    <p class="loc-name">NORTH KENTUCKY - BURLINGTON</p>
    <p>2240 Harbor Point Dr, Burlington,<br>KY 41005, United States</p>
    <p class="loc-name loc-gap">CENTRAL KENTUCKY - RICHMOND</p>
    <p>418 &amp; 420 Linden Ridge Dr, Richmond,<br>KY 40475</p>
  </div>

  <div class="contact-icon" style="left:334px;top:716px">
    <svg viewBox="0 0 24 24" fill="#fff" aria-hidden="true"><path d="M6.6 10.8a15 15 0 0 0 6.6 6.6l2.2-2.2c.3-.3.7-.4 1-.2 1.1.4 2.3.6 3.6.6.6 0 1 .4 1 1V20c0 .6-.4 1-1 1A17 17 0 0 1 3 4c0-.6.4-1 1-1h3.5c.6 0 1 .4 1 1 0 1.3.2 2.5.6 3.6.1.3 0 .7-.2 1z"/></svg>
  </div>
  <p class="contact-line" style="top:716px">859-555-0142<br>859-555-0187</p>

  <div class="contact-icon" style="left:334px;top:754px">
    <svg viewBox="0 0 24 24" fill="none" stroke="#fff" stroke-width="2" aria-hidden="true"><rect x="3" y="5" width="18" height="14" rx="1"/><path d="M3 6l9 7 9-7"/></svg>
  </div>
  <p class="contact-line" style="top:754px">admissions@morvalcare.org</p>

  <div class="contact-icon" style="left:334px;top:786px">
    <svg viewBox="0 0 24 24" fill="none" stroke="#fff" stroke-width="1.8" aria-hidden="true"><circle cx="12" cy="12" r="9"/><path d="M3 12h18M12 3c3 3 3 15 0 18M12 3c-3 3-3 15 0 18"/></svg>
  </div>
  <p class="contact-line" style="top:785px">www.morvalcare.org</p>

  <div class="bottom-band"></div>
</main>
</body>
</html>
```